Lotus Ridge Website

We need a website that has clean, asian looking images that relax and motivate people to come into our integrated medical center. My current website is www.needlebalmclinic.com and I would like the design for Lotus Ridge Health Solutions to be similar but more inviting with video content and a product purchase store as well. A moving banner would be nice too. When people are looking for ways of losing weight or getting out of pain we want them to make the connection that we have the solution. This website needs to provide sufficient information so that patients are well informed and choose us as their health provider before they ever walk through our doors. We offer comprehensive natural medicine that is based on the principles that the body can heal itself when given the right conditions. Our services include medical weight loss and hormone balancing, acupuncture and chinese herbal medicine, physical medicine, trigger point injections, allergy testing and joint rehabilitation. The Medical Doctor and Licensed Acupuncturist work as a team to provide optimal care that is catered to each individual who comes through our doors.
Updates

Target Market(s)

40 to 50 year olds who want to lose weight or have pain issues.

Industry/Entity Type

Medical

Requirements
Must have
• Use photos from our website www.needlebalmclinic.com or similar content. Video content. Moving banner with relaxing images.
Nice to have
• Happy, healthy looking people. Medical Doctors working as a team. Friendly staff in a cutting edge facility.
Should not have
• Papyrus font, or big bold words.

```html
<!DOCTYPE html>
<html lang="en">
<head>
<meta charset="utf-8">
<title>Lotus Ridge Health Solutions</title>
<link href="https://fonts.googleapis.com/css2?family=Roboto+Condensed:ital,wght@0,400;0,700;1,700&family=Roboto:wght@400;700&family=Noto+Serif:wght@400&display=swap" rel="stylesheet">
<style>
:root{
  --topbar:#8b6f4c;
  --brown:#5d3f2c;
  --gold:#ae8a50;
  --panel:#cdb996;
  --strip:#c8b28d;
  --nav:#7a583c;
  --nav-dark:#6a4a31;
  --title:#c3a57a;
  --red:#e03a27;
  --text:#4d3a2a;
  --muted:#9b8258;
  --box:#8b6f4c;
  --white:#ffffff;
}
*{margin:0;padding:0;box-sizing:border-box}
html,body{width:993px;height:1200px;overflow:hidden;background:var(--brown)}
.stage{position:relative;width:1200px;height:1450px;transform:scale(.8275);transform-origin:0 0;font-family:Roboto,Arial,sans-serif;color:var(--text)}
.abs{position:absolute}
.topbar{left:0;top:0;width:1200px;height:29px;background:var(--topbar);font-size:9px;color:#f4ead8}
.topbar .date{left:132px;top:9px}
.topbar .links{right:134px;top:9px}
.topbar b{font-weight:700}
.head{left:0;top:29px;width:1200px;height:306px;background:var(--brown)}
.pattern{left:0;top:335px;width:1200px;height:985px;background:linear-gradient(90deg,#b59257,#a9854a 50%,#b59257)}
.brand{left:132px;top:58px;font-family:"Roboto Condensed",sans-serif;font-size:36px;color:var(--title);letter-spacing:-.3px}
.search{left:870px;top:69px;width:206px;height:30px;background:var(--white);border-radius:3px;font-size:14px;color:#888;padding:7px 10px}
.search .btn{position:absolute;right:0;top:0;width:29px;height:30px;background:var(--red);border-radius:0 3px 3px 0}
.nav{left:118px;top:123px;width:964px;height:45px;background:linear-gradient(var(--nav),var(--nav-dark));border-radius:8px 8px 0 0;display:flex;font-family:"Roboto Condensed",sans-serif;font-size:17px;color:#f1e6d2}
.nav span{display:flex;align-items:center;justify-content:center;border-right:1px solid #5a3d27;height:100%}
.nav span.active{color:#1a1008;font-weight:700}
.banner{left:118px;top:167px;width:964px;height:294px;background:linear-gradient(180deg,#cdb791,#9e8c72 70%,#7e705e)}
.strip{left:118px;top:461px;width:964px;height:52px;background:var(--strip)}
.dots{left:178px;top:478px;display:flex;gap:6px}
.dots i{width:16px;height:16px;border-radius:50%;background:#ddd;border:1px solid #999}
.dots i.on{background:var(--red)}
.caption{left:295px;top:472px;width:610px;white-space:nowrap;overflow:hidden;font-family:"Roboto Condensed",sans-serif;font-style:italic;font-weight:700;font-size:20px;color:#5b3f2a;letter-spacing:.7px}
.more{left:927px;top:470px;width:92px;height:29px;background:var(--red);color:#fff;font-weight:700;font-size:17px;letter-spacing:1.5px;text-align:center;line-height:29px}
.panel{left:120px;top:512px;width:960px;height:806px;background:var(--panel)}
.shadow{left:140px;top:513px;width:920px;height:30px;background:radial-gradient(ellipse at 50% 0,rgba(60,40,20,.55),rgba(60,40,20,0) 70%)}
h1{left:202px;top:566px;font-size:31px;color:var(--red);letter-spacing:1.5px;font-weight:700}
.p{font-size:14.5px;line-height:22px;letter-spacing:.9px;color:var(--text)}
.photo-needle{left:200px;top:778px;width:184px;height:394px;background:linear-gradient(135deg,#d9cebb,#a89a85 60%,#7e705f)}
.btn-light{background:#fff;border:1px solid #c9c0b0;border-radius:3px;font-family:"Noto Serif",serif;font-size:14px;color:#4d3a2a;text-align:center}
.newsletter{left:198px;top:1195px;width:453px;height:95px;background:var(--box);border-radius:4px}
.newsletter h3{position:absolute;left:18px;top:17px;font-size:19px;color:#fff;font-weight:700}
.field{position:absolute;top:48px;height:25px;background:#fff;border-radius:3px;font-size:10px;color:#888;padding:7px 12px}
.sub{position:absolute;left:319px;top:48px;width:92px;height:26px;background:var(--red);border-radius:3px;color:#fff;font-weight:700;font-size:15px;text-align:center;line-height:26px}
.herbs{left:720px;top:572px;width:300px;height:195px;background:radial-gradient(circle at 40% 50%,#a87a3a,#6b5428 60%,#4a3a20);border:1px solid #b8a37a}
.herb-cap{left:723px;top:776px;font-size:14.5px;font-style:italic;color:var(--muted);letter-spacing:.9px}
.video{left:718px;top:827px;width:301px;height:227px;background:linear-gradient(#6e6e6e,#555)}
.play{left:837px;top:900px;width:62px;height:62px;border-radius:50%;background:#e6e6e6;border:3px solid #fff}
.ctrl{left:718px;top:1034px;width:301px;height:20px;background:linear-gradient(#e0e0e0,#9a9a9a)}
h2{left:736px;top:1086px;font-size:23px;color:var(--red);font-weight:700}
.news-rule{left:720px;top:1116px;width:290px;height:1px;background:#bda985}
.news{left:719px;top:1122px;font-size:12.5px;letter-spacing:.7px;color:var(--text);list-style:none;white-space:nowrap}
.news li{height:25.5px}
.news li::before{content:">";color:var(--red);font-size:10px;margin-right:8px}
.foot{left:0;top:1318px;width:1200px;height:132px;background:var(--brown);border-top:4px solid #7b5a3e}
.foot-nav{left:125px;top:1355px;font-family:"Roboto Condensed",sans-serif;font-size:12px;color:#a8875a}
.foot-nav b{color:#c9a874}
.copy{left:125px;top:1375px;font-family:"Roboto Condensed",sans-serif;font-size:12px;color:#a8875a}
.social{left:917px;top:1359px;display:flex;gap:6px}
.social i{width:30px;height:30px;background:#f3ead7;border-radius:5px}
</style>
</head>
<body>
<div class="stage">
  <div class="abs topbar">
    <span class="abs date">Monday, February 27, 2012 . 13:14PM</span>
    <span class="abs links">ENG ▾ &nbsp; <b>Login</b> &nbsp;| &nbsp;Register &nbsp;| &nbsp;FAQ</span>
  </div>
  <div class="abs head"></div>
  <div class="abs pattern" role="img" aria-label="Repeating gold oriental lattice pattern"></div>

  <div class="abs brand">Lotus Ridge Health Solutions</div>
  <div class="abs search">Search...
    <span class="btn"><svg width="29" height="30" viewBox="0 0 29 30"><circle cx="13" cy="12" r="5" fill="none" stroke="#fff" stroke-width="2.5"/><line x1="16" y1="16" x2="21" y2="22" stroke="#fff" stroke-width="3" stroke-linecap="round"/></svg></span>
  </div>

  <nav class="abs nav">
    <span class="active" style="width:87px">HOME</span>
    <span style="width:108px">SO TAI HO</span>
    <span style="width:133px">SEITAI SHINPO</span>
    <span style="width:140px">ACUPUNCTURE</span>
    <span style="width:125px">BIOGRAPHY</span>
    <span style="width:118px">NUTRITION</span>
    <span style="width:123px">MY JOURNEY</span>
    <span style="width:130px;border:none">CONTACT US</span>
  </nav>

  <div class="abs banner" role="img" aria-label="Sepia banner photo of a team of seven smiling doctors and nurses in white coats"></div>
  <div class="abs strip"></div>
  <div class="abs dots"><i class="on"></i><i></i><i></i><i></i></div>
  <div class="abs caption">Praesent justo dolor, lobortis quis, lobortis dignissim, pulvinar ac.</div>
  <div class="abs more">MORE</div>

  <div class="abs panel"></div>
  <div class="abs shadow"></div>

  <h1 class="abs">Welcome To LRHS</h1>
  <p class="abs p" style="left:200px;top:604px;width:470px">Aliquam congue fermentum nisl. Mauris accumsan nulla vel diam. Sed in lacus ut enim adipiscing aliquet.</p>
  <p class="abs p" style="left:200px;top:671px;width:462px">Nulla venenatis. In pede mi, aliquet sit amet, euismod in, auctor ut, ligula. Aliquam dapibus tincidunt metus. Praesent justo dolor, lobortis quis, lobortis dignissim, pulvinar ac, lorem. Vestibulum sed ante. Donec sagittis euismod purus.</p>

  <div class="abs photo-needle" role="img" aria-label="Close-up sepia photo of an acupuncture needle being placed"></div>
  <p class="abs p" style="left:410px;top:775px;width:250px">Aliquam congue fermentum nisl. Mauris accumsan nulla vel diam. Sed in lacus ut enim adipiscing aliquet.</p>
  <p class="abs p" style="left:410px;top:885px;width:250px">Nulla venenatis. In pede mi, aliquet sit amet, euismod in, auctor ut, ligula. Aliquam dapibus tincidunt metus. Praesent justo dolor, lobortis quis, lobortis dignissim, pulvinar ac, lorem. Vestibulum sed ante. Donec sagittis euismod purus.</p>
  <p class="abs p" style="left:410px;top:1083px;width:250px">Aliquam congue fermentum nisl. Mauris accumsan nulla vel diam.</p>
  <div class="abs btn-light" style="left:406px;top:1141px;width:94px;height:32px;line-height:30px">Read More</div>

  <div class="abs newsletter">
    <h3>Join our Newsletter</h3>
    <div class="field" style="left:15px;width:142px">Name:</div>
    <div class="field" style="left:165px;width:142px">Email:</div>
    <div class="sub">Subscribe</div>
  </div>

  <div class="abs herbs" role="img" aria-label="Bowls of dried Chinese herbs on a wooden table with brushed calligraphy"></div>
  <div class="abs herb-cap">In pede mi, aliquet sit amet, euismod in.</div>

  <div class="abs video" role="img" aria-label="Video still of three doctors in white coats"></div>
  <div class="abs play"><svg width="56" height="56" viewBox="0 0 56 56"><polygon points="21,16 42,28 21,40" fill="#8a8a8a"/></svg></div>
  <div class="abs ctrl">
    <svg width="301" height="20" viewBox="0 0 301 20">
      <rect x="6" y="5" width="4" height="10" fill="#444"/><rect x="12" y="5" width="4" height="10" fill="#444"/>
      <rect x="26" y="5" width="2" height="10" fill="#444"/><polygon points="36,5 29,10 36,15" fill="#444"/>
      <circle cx="47" cy="10" r="4" fill="#eee" stroke="#666"/>
      <line x1="52" y1="10" x2="140" y2="10" stroke="#333" stroke-width="2"/>
      <rect x="146" y="5" width="46" height="10" fill="#222"/>
      <line x1="202" y1="10" x2="236" y2="10" stroke="#333" stroke-width="2"/>
      <polygon points="240,8 244,8 249,4 249,16 244,12 240,12" fill="#444"/>
      <rect x="264" y="6" width="12" height="8" fill="#666"/><rect x="282" y="6" width="12" height="8" fill="#666"/>
    </svg>
  </div>

  <h2 class="abs">LRHS Latest News</h2>
  <div class="abs news-rule"></div>
  <ul class="abs news">
    <li>Aliquam dapibus tincidunt metus donec sagittis</li>
    <li>Praesent justo dolor sagittis euismod purus</li>
    <li>Vestibulum sed ante</li>
    <li>Donec sagittis euismod purus</li>
    <li>Praesent justo dolor sagittis euismod purus</li>
  </ul>
  <div class="abs btn-light" style="left:732px;top:1254px;width:90px;height:30px;line-height:28px">See More</div>

  <footer class="abs foot"></footer>
  <div class="abs foot-nav"><b>HOME</b> &nbsp;| &nbsp;SO TAI HO &nbsp;| &nbsp;SEITAI SHINPO &nbsp;| &nbsp;ACUPUNCTURE &nbsp;| &nbsp;BIOGRAPHY &nbsp;| &nbsp;NUTRITION &nbsp; | &nbsp;MY JOURNEY &nbsp;| &nbsp;CONTACT US</div>
  <div class="abs copy">Copyright © 2012 &nbsp;Lotus Ridge Health Solutions. &nbsp;All Rights Reserved.</div>
  <div class="abs social"><i></i><i></i><i></i><i></i></div>
</div>
</body>
</html>
```